Asia based real estate financing firm needs and AWESOME design for a biz card -Harbor Lending Circle

Looking for a stylish, & corporate-looking business card for a real estate financing brokerage firm in Asia, offering global mortgage loans. I uploaded our current logos. We would like to add a splash of color (perhaps the house icon) or any other suggestions are open. For the winning designer, we have a lot of work! Thanks and best of luck!

Target Market(s)

Real estate investors globally. We want to look more like a BANK and NOT a real estate company. Please don't play up on a "house" design.

Industry/Entity Type

Banking

Contact Information for Business Card

Harbor Lending Circle
Peter Wilks
Co-Founder | Partner

14 Cassia Lane, Suite 310
Singapore 047219
www.hlc-example.asia
peterwilks@hlc-example.asia
+65 555-0142
WeChat: peterwilks

Colors

Designer to choose colors to be used in the design.

Requirements
Must have
• Must have the standard business requirements for a card; name, address, email, etc
• Can be horizontal or vertical.
Nice to have
• It would be great to see some sort of variation to the logo with a pop of color. Red is good as we're in Asia, however, other options work as well.
• Our tag line is - Lending Without Limits. It doesn't have to be on the card but might be nice.
• I'd like to start seeing our tagline within the cards as well. - Lending Without Limits.
• Also, please add our location. The location for this card is Singapore so perhaps it can be highlighted or emphasised in some way.
• Singapore | Hong Kong | Shanghai | Manila
• As we will soon open an office in Shanghai, having an option for both languages would be great.
Should not have
• I'm exceited and open to your creativity ... knock it out of the park!

```html
<!DOCTYPE html>
<html lang="en">
<head>
<meta charset="utf-8">
<title>Harbor Lending Circle – Business Card</title>
<link rel="stylesheet" href="https://fonts.googleapis.com/css2?family=Cinzel:wght@400;500&family=Cormorant+Garamond:ital,wght@1,500&family=Open+Sans:wght@400&display=swap">
<style>
  :root {
    --backdrop: #2b2b2b;
    --card: #151515;
    --card-edge: #1f1f1f;
    --ink: #f2f2f2;
    --ink-soft: #d9d9d9;
    --accent: #c1121f;
  }
  * { margin: 0; padding: 0; box-sizing: border-box; }
  html, body {
    width: 1200px; height: 716px; overflow: hidden;
    background: var(--backdrop);
  }
  .stage {
    position: relative; width: 1200px; height: 716px;
    display: flex; align-items: center; justify-content: center; gap: 50px;
  }
  .card {
    position: relative; width: 525px; height: 300px;
    background: var(--card);
    border: 1px solid var(--card-edge);
    border-radius: 18px;
    overflow: hidden;
  }

  /* Front */
  .front {
    display: flex; flex-direction: column; align-items: center; justify-content: center;
  }
  .front .brand-name {
    font-family: "Cinzel", serif; font-weight: 500;
    font-size: 34px; line-height: 1.15; letter-spacing: 1px;
    color: var(--ink); text-align: center;
  }
  .front .tagline {
    margin-top: 22px;
    font-family: "Cinzel", serif; font-weight: 400;
    font-size: 15px; letter-spacing: 4px;
    color: var(--accent);
  }

  /* Back */
  .back .person { position: absolute; left: 34px; top: 62px; }
  .back .person-name {
    font-family: "Cinzel", serif; font-weight: 400;
    font-size: 22px; letter-spacing: 1px; color: var(--ink);
  }
  .back .person-title {
    font-family: "Cormorant Garamond", serif; font-style: italic; font-weight: 500;
    font-size: 14px; color: var(--accent); margin-top: 1px;
  }
  .back .rule {
    position: absolute; left: 150px; right: 0; top: 108px;
    height: 1.5px; background: var(--accent);
  }
  .back .contacts {
    position: absolute; left: 34px; top: 128px;
    list-style: none;
    font-family: "Open Sans", sans-serif; font-size: 12.5px; color: var(--ink-soft);
  }
  .back .contacts li { display: flex; align-items: center; gap: 8px; height: 22px; }
  .back .contacts svg { width: 12px; height: 12px; flex: none; }
  .back .brand-name {
    position: absolute; right: 34px; top: 34px; width: 200px;
    font-family: "Cinzel", serif; font-weight: 500;
    font-size: 20px; line-height: 1.2; text-align: right;
    color: var(--accent);
  }
  .back .address {
    position: absolute; right: 30px; bottom: 26px;
    list-style: none; text-align: right;
    font-family: "Open Sans", sans-serif; font-size: 13px; color: var(--ink);
  }
  .back .address li { display: flex; align-items: center; justify-content: flex-end; gap: 8px; height: 22px; }
  .back .address svg { width: 13px; height: 13px; flex: none; }
  .icon-slot { width: 13px; flex: none; }
</style>
</head>
<body>
<main class="stage">

  <section class="card front" aria-label="Card front">
    <h1 class="brand-name">Harbor Lending<br>Circle</h1>
    <p class="tagline">LENDING WITHOUT LIMITS</p>
  </section>

  <section class="card back" aria-label="Card back">
    <div class="person">
      <h2 class="person-name">PETER WILKS</h2>
      <p class="person-title">Co-Founder | Partner</p>
    </div>
    <div class="rule"></div>

    <p class="brand-name">Harbor Lending Circle</p>

    <ul class="contacts">
      <li>
        <svg viewBox="0 0 24 24" aria-hidden="true" fill="var(--accent)"><path d="M6.6 10.8a15.1 15.1 0 0 0 6.6 6.6l2.2-2.2c.3-.3.7-.4 1-.2 1.1.4 2.3.6 3.6.6.6 0 1 .4 1 1V20c0 .6-.4 1-1 1C10.6 21 3 13.4 3 4c0-.6.4-1 1-1h3.5c.6 0 1 .4 1 1 0 1.3.2 2.5.6 3.6.1.3 0 .7-.2 1z"/></svg>
        +65 555-0142
      </li>
      <li>
        <svg viewBox="0 0 24 24" aria-hidden="true" fill="none" stroke="var(--accent)" stroke-width="2.4"><rect x="2.5" y="5" width="19" height="14" rx="1"/><path d="M3 6l9 7 9-7"/></svg>
        peterwilks@hlc-example.asia
      </li>
      <li>
        <svg viewBox="0 0 24 24" aria-hidden="true" fill="var(--accent)"><path d="M12 3C6.5 3 2 6.8 2 11.5c0 2.4 1.2 4.6 3.1 6.1L4 21l4.2-2.1c1.2.4 2.5.6 3.8.6 5.5 0 10-3.8 10-8.5S17.5 3 12 3z"/></svg>
        peterwilks
      </li>
    </ul>

    <ul class="address">
      <li>14 Cassia Lane, Suite 310<span class="icon-slot"></span></li>
      <li>Singapore 047219
        <svg viewBox="0 0 24 24" aria-hidden="true"><path fill="var(--accent)" d="M12 2a7 7 0 0 0-7 7c0 5 7 13 7 13s7-8 7-13a7 7 0 0 0-7-7zm0 9.5A2.5 2.5 0 1 1 12 6.5a2.5 2.5 0 0 1 0 5z"/></svg>
      </li>
      <li>www.hlc-example.asia
        <svg viewBox="0 0 24 24" aria-hidden="true" fill="none" stroke="var(--accent)" stroke-width="2"><circle cx="12" cy="12" r="9.5"/><path d="M2.5 12h19M12 2.5c3 3 3 16 0 19M12 2.5c-3 3-3 16 0 19"/></svg>
      </li>
    </ul>
  </section>

</main>
</body>
</html>
```